Stationary for Marigold Spa
Business Card, Envelope, & Letterhead
Project: Stationary for Marigold Spa
Stationary for Marigold Spa -
Creative Brief
Simple
use logo no person's name
27815 Orchard Blvd. Ste 342 San Antonio, TX 78259
hbt4726@quillpost.net
We don't have the website yet. Please do not use the email on the project. On the business card front side, we only need our logo, address, phone no. Back side will be the services that we will provide.
Acupressure, Tui Na, Deep Tissue Massage, Swedish Massage, Prenatal Massage, Reflexology, Traditional Herbal Foot Treatment

```html
<!DOCTYPE html>
<html lang="en">
<head>
<meta charset="utf-8">
<title>Marigold Spa – Business Card</title>
<link rel="stylesheet" href="https://fonts.googleapis.com/css2?family=Questrial&family=Jost:wght@500&display=swap">
<style>
  :root {
    --backdrop: #e9e6e1;
    --card: #ffffff;
    --leaf: #b3bb1f;
    --stone: #6d6e71;
    --rule: #a7a9ac;
    --ink: #2b2b2b;
  }
  html, body {
    margin: 0;
    width: 1200px;
    height: 780px;
    overflow: hidden;
    background: var(--backdrop);
  }
  .canvas {
    position: relative;
    width: 1200px;
    height: 780px;
  }
  .business-card {
    position: absolute;
    left: 150px;
    top: 133px;
    width: 900px;
    height: 514px;
    background: var(--card);
    border-radius: 26px;
    box-shadow: 0 10px 30px rgba(0,0,0,0.18);
    overflow: hidden;
  }
  .accent-band {
    position: absolute;
    left: 20px;
    top: 0;
    width: 28px;
    height: 100%;
    background: var(--leaf);
  }
  .accent-rule {
    position: absolute;
    left: 54px;
    top: 0;
    width: 4px;
    height: 100%;
    background: var(--rule);
  }
  .brand {
    position: absolute;
    left: 250px;
    top: 170px;
    font-family: "Questrial", sans-serif;
  }
  .brand-name {
    margin: 0;
    font-size: 66px;
    font-weight: 400;
    letter-spacing: -1px;
    color: var(--stone);
    line-height: 1;
  }
  .brand-tagline {
    margin: 6px 0 0 150px;
    font-size: 26px;
    color: var(--stone);
  }
  .phone {
    position: absolute;
    left: 300px;
    top: 318px;
    display: flex;
    align-items: center;
    gap: 12px;
    font-family: "Questrial", sans-serif;
    font-size: 40px;
    color: var(--stone);
  }
  .phone-icon {
    width: 38px;
    height: 38px;
  }
  .address {
    position: absolute;
    left: 220px;
    top: 424px;
    margin: 0;
    font-family: "Jost", sans-serif;
    font-weight: 500;
    font-size: 18px;
    letter-spacing: 0.3px;
    color: var(--ink);
  }
</style>
</head>
<body>
<main class="canvas">
  <section class="business-card" aria-label="Marigold Spa business card front">
    <div class="accent-band"></div>
    <div class="accent-rule"></div>

    <div class="brand">
      <h1 class="brand-name">Marigold Spa</h1>
      <p class="brand-tagline">Health Relaxation</p>
    </div>

    <div class="phone">
      <svg class="phone-icon" viewBox="0 0 38 38" aria-hidden="true">
        <circle cx="19" cy="19" r="16.5" fill="none" stroke="#b3bb1f" stroke-width="3"/>
        <path d="M13 11 l4 -1 l2 5 l-2.5 2 q2 4.5 6 6.5 l2 -2.5 l5 2 l-1 4 q-1 1.5 -3 1 q-9 -2.5 -13.5 -13 q-0.5 -2.5 1 -4z" fill="#b3bb1f"/>
      </svg>
      <span class="phone-number">(210)555-0147</span>
    </div>

    <p class="address">27815 Orchard Blvd. Ste 342 San Antonio, TX 78259</p>
  </section>
</main>
</body>
</html>
```